Summit Motion Academy Brochure & Business Card Design

Requirements: Summit Motion Academy (SMA) seeks to work with ArtHive in order to produce a clean, simple, and high-class design that can be applied to multiple types of marketing collateral. We would like any design to be based on our logo (attached below) and its appropriate color schemes (silver, red, white, and black). We anticipate the creation of a design that will be consistent and appropriate for:
- Accordion fold brochure (6 panels, dimensions approximately 5” x 7”, please avoid standard tri-fold pamphlet layout)
-Business cards (double-sided)

Other attachments in this brief include: Adobe Illustrator files featuring various arrangements of the SMA logo, PDF file showing all variations of SMA logo, professional images (.jpg) that can be incorporated into a brochure design where appropriate

Background information: Summit Motion Academy is a service-based business that dedicated to enhancing the physical performance of our athletes. Serving juniors, collegiate athletes, amateurs, and professionals alike, the team at SMA presents a disciplined and innovative perspective on the overall facets of health and well-being. Behind SMA’s certified performance specialist, Brent Lowry, the team is excited to find a stylish design that invokes the strong, stable, and balanced principles that are at the foundation of not only the Institute’s logo and coaching strategy, but are also the main focuses our commercial outlook as a whole.

NOTE: Please visit our company website: summitmoa.com for more information and links to our social media accounts where you can learn a bit more about our company! In addition, if you'd like to know more about anticipated text content for the brochures, please contact me at tselby@summitmoa.com

Project Deadline Extended
Reason: Project deadline is being extended to allow more time for designing with the goal of increasing participation in our contest. Files have been added to our brief giving more detail about content within our brochure. Thank you, and we look forward to seeing some more great designs!

Target Market(s)

Athletes in lines of service including: elite junior development, collegiate and amateur performance, and professional maintenance

Industry/Entity Type

Business

Contact Information for Business Card

Brent Lowry, Director of Performance
Summit Motion Academy
(555) 418-2937
blowry@summitmoa.com
summitmoa.com (website)
@summitmoa (social media icons for Chirpnet, Friendspace, and Linkly+)

Font styles to use
Serif
Sans Serif

Requirements
Must have
• Brochure: approximately 5" x 7" dimensions, accordion fold
• Colors: refer to color schemes in company logo documents
Nice to have
• Business card: Motto or tagline "Reach Your True Potential"
• Business card: background color could be silver or grayscale
• Font: Font style follows Greek influence of company logo and symbol
• Graphics: please refer to the following links for some examples of anatomy/biomechanics graphics that could be included in marketing collateral:
• http://www.printvora.com/studio.aspx?template=8830417_K21_058&ag=True&ag_category_id=913&xnav=previews&xnid=image_472&rd=1
• http://fibermotionlab.com
Should not have
• Brochure: Do not have standard tri-fold pamphlet layout

```html
<!DOCTYPE html>
<html lang="en">
<head>
<meta charset="utf-8">
<title>Summit Motion Academy – Accordion Brochure</title>
<link href="https://fonts.googleapis.com/css2?family=Open+Sans:wght@600&family=Cinzel:wght@500&display=swap" rel="stylesheet">
<style>
  :root {
    --red: #e0242b;
    --black: #231f20;
    --silver: #8f8f90;
    --white: #ffffff;
    --band-gray: rgba(140,140,140,0.85);
    --band-red: rgba(214,36,43,0.9);
    --band-dark: rgba(50,50,50,0.85);
    --stage: #ffffff;
  }
  * { box-sizing: border-box; margin: 0; padding: 0; }
  html, body { width: 1200px; height: 743px; overflow: hidden; background: var(--stage); }
  .brochure {
    position: absolute; left: 30px; top: 161px;
    width: 1140px; height: 420px;
    display: grid; grid-template-columns: repeat(6, 1fr);
    box-shadow: 0 6px 24px rgba(0,0,0,0.18);
  }
  .panel { display: grid; grid-template-rows: 1fr 1fr; }
  .half { position: relative; overflow: hidden; }
  .half.upper { border-bottom: 2px dotted rgba(255,255,255,0.7); }
  .solid-red { background: var(--red); }
  .solid-black { background: var(--black); }
  .solid-silver { background: var(--silver); }
  .brand-mark {
    position: absolute; inset: 0;
    display: flex; flex-direction: column; align-items: center; justify-content: center; gap: 10px;
  }
  .brand-mark .dot {
    width: 54px; height: 54px; border-radius: 50%;
    border: 3px solid var(--white);
  }
  .brand-mark .initials {
    font-family: "Cinzel", serif; font-weight: 500; font-size: 22px;
    color: var(--white); letter-spacing: 3px;
  }
  .photo { position: absolute; inset: 0; }
  .photo-storm { background: linear-gradient(135deg, #3b4653 0%, #5e6a76 45%, #8a2b2b 100%); }
  .photo-yoga { background: linear-gradient(160deg, #3f7a2c 0%, #6da53e 55%, #b98b6a 100%); }
  .photo-spice { background: linear-gradient(150deg, #4a2b1f 0%, #6b4530 50%, #a0351f 100%); }
  .photo-trail { background: linear-gradient(180deg, #c9d3cf 0%, #6d8a3e 50%, #a98963 100%); }
  .photo-hiker { background: linear-gradient(160deg, #b7c9d6 0%, #d9c7a5 55%, #c23a44 100%); }
  .photo-golf { background: linear-gradient(180deg, #2e7fd0 0%, #6aa6e0 55%, #2c4a7a 100%); }
  .caption {
    position: absolute; font-family: "Open Sans", sans-serif; font-weight: 600;
    font-size: 13px; color: var(--white); letter-spacing: -0.2px;
  }
  .name-band {
    position: absolute; left: 0; right: 0; height: 30px;
    display: flex; align-items: center; justify-content: center;
    font-family: "Cinzel", serif; font-weight: 500; font-size: 10px;
    color: var(--white); letter-spacing: 0.5px; text-align: center;
  }
  .band-gray { background: var(--band-gray); }
  .band-red { background: var(--band-red); }
  .band-dark { background: var(--band-dark); }
</style>
</head>
<body>
<main class="brochure">

  <section class="panel">
    <div class="half upper">
      <div class="photo photo-storm" role="img" aria-label="Sprinter in a red jacket running under a stormy sky with lightning"></div>
      <span class="caption" style="left:18px; top:24px;">Be Energized</span>
      <div class="name-band band-gray" style="top:118px;">Summit Motion Academy</div>
    </div>
    <div class="half solid-black">
      <div class="brand-mark"><span class="dot"></span><span class="initials">SMA</span></div>
    </div>
  </section>

  <section class="panel">
    <div class="half upper solid-red">
      <div class="brand-mark"><span class="dot"></span><span class="initials">SMA</span></div>
    </div>
    <div class="half">
      <div class="photo photo-yoga" role="img" aria-label="Family meditating outdoors in front of green trees"></div>
      <span class="caption" style="right:14px; top:14px;">Be Balanced</span>
      <div class="name-band band-red" style="top:118px;">Summit Motion Academy</div>
    </div>
  </section>

  <section class="panel">
    <div class="half upper">
      <div class="photo photo-spice" role="img" aria-label="Cinnamon sticks and spices on a dark wooden table"></div>
      <span class="caption" style="right:16px; top:52px;">Be Nutritious</span>
      <div class="name-band band-gray" style="top:120px;">Summit Motion Academy</div>
    </div>
    <div class="half solid-silver">
      <div class="brand-mark"><span class="dot"></span><span class="initials">SMA</span></div>
    </div>
  </section>

  <section class="panel">
    <div class="half upper solid-black">
      <div class="brand-mark"><span class="dot"></span><span class="initials">SMA</span></div>
    </div>
    <div class="half">
      <div class="photo photo-trail" role="img" aria-label="Runner's legs striding along a dirt trail"></div>
      <span class="caption" style="right:14px; top:16px;">Be Fit</span>
      <div class="name-band band-dark" style="top:100px;">Summit Motion Academy</div>
    </div>
  </section>

  <section class="panel">
    <div class="half upper">
      <div class="photo photo-hiker" role="img" aria-label="Hiker in a red jacket and knit hat on a mountain trail"></div>
      <div class="name-band band-red" style="top:10px; height:24px;">Summit Motion Academy</div>
      <span class="caption" style="left:16px; top:164px;">Be Healthy</span>
    </div>
    <div class="half solid-red">
      <div class="brand-mark"><span class="dot"></span><span class="initials">SMA</span></div>
    </div>
  </section>

  <section class="panel">
    <div class="half upper solid-silver">
      <div class="brand-mark"><span class="dot"></span><span class="initials">SMA</span></div>
    </div>
    <div class="half">
      <div class="photo photo-golf" role="img" aria-label="Golfer finishing a swing against a blue sky"></div>
      <span class="caption" style="right:8px; top:16px; font-size:12px;">Reach Your True Potential</span>
      <div class="name-band band-gray" style="top:140px;">Summit Motion Academy</div>
    </div>
  </section>

</main>
</body>
</html>
```